Website for Apartment Rental in Prague

I would like to create designs of my website focused on luxury apartment rentals in Prague, Czech Republic. I created initial mock-ups, They are all attached. I need to design homepage and subpage. The mock-ups were created by combining elements from different websites that I liked but I need you to create a design that is unique and original. The attached files a only a guidance for the structure of the website but not for the design. Try to be creative.

Industry/Entity Type

Apartment

```html
<!DOCTYPE html>
<html lang="en">
<head>
<meta charset="utf-8">
<title>Maison Lumen Apartments Prague</title>
<link href="https://fonts.googleapis.com/css2?family=Lato:ital,wght@0,400;0,700;0,900;1,400;1,700&family=Playfair+Display:ital@1&display=swap" rel="stylesheet">
<style>
:root{
  --gold:#a27c3f;
  --gold-dark:#8d6a33;
  --ink:#222222;
  --text:#555555;
  --muted:#8a8a8a;
  --line:#dddddd;
  --nav-bg:#f0f0f0;
  --band:#ebebeb;
  --band-warm:#ece6e3;
  --footer:#1e1e1e;
  --footer-bottom:#151515;
  --white:#ffffff;
}
*{box-sizing:border-box;margin:0;padding:0}
html,body{width:1200px;height:4054px;overflow:hidden}
body{font-family:"Lato",sans-serif;color:var(--ink);background:var(--white);position:relative}
.abs{position:absolute}

/* Header */
.topbar{position:absolute;left:0;top:0;width:1200px;height:119px}
.topbar .hospitality{left:76px;top:50px;font-size:13px;color:var(--gold);font-weight:700;letter-spacing:.5px}
.topbar .lang{left:228px;top:50px;font-size:13px;color:var(--ink);font-weight:700}
.brand{left:0;width:1200px;top:22px;text-align:center}
.brand .name{font-size:22px;font-weight:900;color:var(--gold);letter-spacing:2px}
.brand .sub{font-size:12px;font-weight:700;letter-spacing:2px;color:var(--ink);margin-top:4px}
.brand .url{font-size:11px;color:var(--gold);margin-top:4px}
.topbar .discover{left:733px;top:50px;font-size:13px;font-weight:700;display:flex;align-items:center;gap:10px}
.topbar .contact{left:925px;top:40px;font-size:13px;line-height:30px}
.topbar .contact div{display:flex;align-items:center;gap:8px}
.topbar .contact .phone{color:var(--gold);font-weight:700;font-size:15px}
.nav{position:absolute;left:0;top:119px;width:1200px;height:59px;background:var(--nav-bg);border-top:1px solid var(--line);display:flex;justify-content:space-around;align-items:center;padding:0 60px;font-size:13px;font-weight:700;letter-spacing:.4px}

/* Hero */
.hero{position:absolute;left:0;top:178px;width:1200px;height:607px;background:linear-gradient(160deg,#5a5a5a 0%,#3a3a3a 45%,#2a2a2a 100%)}
.hero h1{position:absolute;top:145px;width:100%;text-align:center;color:var(--white);font-size:58px;font-weight:700;letter-spacing:1px}
.dots{position:absolute;top:320px;width:100%;display:flex;justify-content:center;gap:12px}
.dots span{width:11px;height:11px;border-radius:50%;background:var(--white)}
.booking{position:absolute;left:76px;top:554px;width:1048px;height:216px;background:var(--white);box-shadow:0 4px 18px rgba(0,0,0,.15)}
.booking h2{position:absolute;top:30px;width:100%;text-align:center;color:var(--gold);font-size:24px;font-weight:700;letter-spacing:1px;display:flex;justify-content:center;align-items:center;gap:18px}
.booking h2 i{display:block;width:40px;height:2px;background:var(--gold)}
.field{position:absolute;height:42px;border:1px solid var(--line);border-radius:21px;font-size:12px;color:var(--text);display:flex;align-items:center;justify-content:space-between;padding:0 16px;white-space:nowrap}
.field svg{flex:none}
.booking .or{position:absolute;left:479px;top:150px;font-size:15px;font-weight:700}
.btn-check{position:absolute;left:711px;top:138px;width:221px;height:42px;border-radius:21px;background:#1c1c1c;color:var(--white);font-size:15px;font-weight:700;display:flex;align-items:center;justify-content:center}

/* Intro */
.intro{position:absolute;left:0;top:830px;width:1200px;text-align:center}
.intro h2{font-size:34px;font-weight:700;line-height:44px;letter-spacing:.5px}
.intro p{width:740px;margin:38px auto 0;font-size:14px;line-height:26px;color:var(--gold);font-style:italic}

/* Interior */
.interior{position:absolute;left:0;top:1092px;width:1200px;height:403px;background:var(--band)}
.interior h2{position:absolute;left:76px;top:60px;font-size:28px;font-weight:700;letter-spacing:1px}
.interior .by{position:absolute;left:76px;top:100px;font-family:"Playfair Display",serif;font-style:italic;color:var(--gold);font-size:25px}
.interior p{position:absolute;left:76px;top:165px;width:490px;font-size:14px;line-height:25px;color:var(--text)}
.interior .photo{position:absolute;left:600px;top:0;width:600px;height:403px;background:linear-gradient(135deg,#e9e6e1,#b9aa95 60%,#6e5a45)}

/* Featured */
.featured-title{position:absolute;top:1545px;width:1200px;text-align:center;font-size:32px;font-weight:700;letter-spacing:.5px}
.cards{position:absolute;left:76px;width:1048px;display:grid;grid-template-columns:repeat(3,332px);column-gap:26px}
.card .img{position:relative;height:190px;background:linear-gradient(150deg,#8b7359,#4a3d30)}
.card:nth-child(2) .img{background:linear-gradient(150deg,#a8957c,#5c4b3a)}
.card:nth-child(3) .img{background:linear-gradient(150deg,#cdbfa8,#7a6a55)}
.card .img .meta{position:absolute;left:14px;bottom:12px;color:var(--white);font-size:12px;font-weight:700;letter-spacing:.4px}
.card h3{margin-top:26px;font-size:15px;line-height:23px;color:var(--gold);font-weight:700;text-transform:uppercase}
.card p{margin-top:14px;font-size:13px;line-height:21px;color:var(--text)}
.card .actions{margin-top:16px;display:flex;gap:12px}
.pill{width:160px;height:42px;border-radius:21px;display:flex;align-items:center;justify-content:center;font-size:13px;font-weight:700}
.pill.gold{background:var(--gold);color:var(--white)}
.pill.outline{border:1px solid #cfcfcf;color:var(--ink)}

/* Need to know */
.need{position:absolute;left:0;top:2554px;width:1200px;height:401px;background:var(--band-warm)}
.need h2{position:absolute;top:50px;width:100%;text-align:center;font-size:28px;font-weight:700}
.need .item{position:absolute;top:145px;width:300px;text-align:center}
.need .circle{width:100px;height:100px;margin:0 auto;border-radius:50%;border:3px solid var(--gold);background:var(--white);display:flex;align-items:center;justify-content:center}
.need h3{margin-top:32px;font-size:16px;font-weight:700;color:var(--gold);letter-spacing:.5px}
.need p{margin-top:10px;font-size:13px;line-height:21px;color:var(--text)}

/* News and testimonials */
.col-title{position:absolute;top:3000px;font-size:28px;font-weight:700}
.news-item{position:absolute;left:76px;width:500px}
.date{position:absolute;left:0;top:0;width:58px;text-align:center}
.date .m{background:var(--gold);color:var(--white);font-size:13px;font-weight:700;height:26px;line-height:26px}
.date .d{background:#1c1c1c;color:var(--white);font-size:34px;font-weight:900;height:54px;line-height:54px}
.news-item h3{margin-left:88px;font-size:16px;font-weight:700;color:var(--gold)}
.news-item p{margin-left:88px;margin-top:8px;font-size:13px;line-height:21px;color:var(--text)}
.news-item p b{color:var(--ink)}
.divider{position:absolute;left:600px;top:3060px;width:1px;height:250px;background:var(--line)}
.arrows{position:absolute;left:1080px;top:3008px;display:flex;gap:18px}
.quote-icon{position:absolute;left:630px;top:3075px;width:52px;height:52px;border-radius:50%;border:2px solid var(--gold);display:flex;align-items:center;justify-content:center;color:var(--gold);font-family:"Playfair Display",serif;font-size:40px;line-height:1;padding-top:14px}
.testimonial{position:absolute;left:712px;top:3065px;width:412px;font-size:13px;line-height:21px;font-style:italic;color:var(--text);border-left:1px solid var(--line);padding-left:20px}
.avatar{position:absolute;left:630px;top:3225px;width:80px;height:80px;border-radius:50%;background:linear-gradient(135deg,#d8c3aa,#8f7660)}
.person{position:absolute;left:740px;top:3245px}
.person b{display:block;font-size:14px;color:var(--gold);font-weight:700}
.person i{font-size:13px;color:var(--text)}

/* As seen in */
.seen{position:absolute;left:0;top:3379px;width:1200px;height:176px;background:var(--band-warm)}
.seen h2{position:absolute;top:38px;width:100%;text-align:center;font-size:18px;font-weight:700;letter-spacing:1px}
.seen .badges{position:absolute;top:96px;left:170px;width:860px;display:flex;justify-content:space-between;align-items:center}
.seen .badges span{display:block;height:28px;background:#9c9591;border-radius:3px;opacity:.7}

/* Newsletter */
.newsletter{position:absolute;left:76px;top:3590px;width:1048px;height:60px;display:flex;align-items:center}
.newsletter h2{font-size:22px;font-weight:700;width:246px}
.signup{position:relative;width:412px;height:46px;border:1px solid #cfcfcf;border-radius:23px;font-size:13px;color:var(--text);display:flex;align-items:center;padding-left:20px}
.signup .go{position:absolute;right:4px;top:4px;width:36px;height:36px;border-radius:50%;background:var(--gold);color:var(--white);font-size:13px;font-weight:700;display:flex;align-items:center;justify-content:center}
.follow{margin-left:auto;display:flex;align-items:center;gap:14px}
.follow h2{width:auto;margin-right:8px}
.follow span{width:22px;height:22px;border-radius:50%;background:var(--gold)}

/* Footer */
.footer{position:absolute;left:0;top:3682px;width:1200px;height:305px;background:var(--footer);color:#cfcfcf}
.footer .brand-name{position:absolute;left:76px;top:50px;font-size:22px;font-weight:900;color:var(--gold);letter-spacing:2px}
.footer .about{position:absolute;left:76px;top:100px;width:300px;font-size:13px;line-height:22px}
.footer h4{font-size:14px;font-weight:700;color:var(--gold);letter-spacing:.5px;margin-bottom:10px}
.footer ul{list-style:none;font-size:13px;line-height:22px}
.footer .sitemap{position:absolute;left:437px;top:50px}
.footer .contact-info{position:absolute;left:660px;top:50px;font-size:13px;line-height:22px;width:190px}
.footer .map{position:absolute;left:860px;top:20px;width:264px;height:165px;background:linear-gradient(135deg,#e4e7e2,#c9d3c6)}
.copyright{position:absolute;left:0;top:3987px;width:1200px;height:67px;background:var(--footer-bottom);color:#8a8a8a;font-size:12px;display:flex;align-items:center;justify-content:center}
</style>
</head>
<body>

<header class="topbar">
  <div class="abs hospitality">OUR HOSPITALITY</div>
  <div class="abs lang">EN &#9662;</div>
  <div class="abs brand">
    <div class="name">MAISON LUMEN</div>
    <div class="sub">APARTMENTS<br>PRAGUE</div>
    <div class="url">maisonlumen.com</div>
  </div>
  <div class="abs discover">
    <svg width="16" height="14" viewBox="0 0 16 14"><path d="M1 0v14M1 1h12l-3 3.5 3 3.5H1" fill="#222" stroke="#222" stroke-width="1.5"/></svg>
    DISCOVER PRAGUE
  </div>
  <div class="abs contact">
    <div class="phone"><svg width="14" height="14" viewBox="0 0 14 14"><path d="M3 1l2.5 3-1.5 1.5c1 2 2.5 3.5 4.5 4.5L10 8.5l3 2.5-1.5 2C6 12.5 1.5 8 1 2.5z" fill="#a27c3f"/></svg>420 600 123 456</div>
    <div><svg width="14" height="11" viewBox="0 0 14 11"><rect x=".5" y=".5" width="13" height="10" fill="none" stroke="#a27c3f"/><path d="M.5 .5l6.5 5.5 6.5-5.5" fill="none" stroke="#a27c3f"/></svg>reservation@maisonlumen.com</div>
  </div>
</header>

<nav class="nav">
  <span>APARTMENTS</span><span>LOCATION</span><span>SERVICES</span><span>GALLERY</span><span>NEWS</span><span>EXCLUSIVE OFFERS &amp; TOURS</span><span>FOR FAMILIES</span><span>CONTACT US</span>
</nav>

<section class="hero" role="img" aria-label="Photo of a luxury apartment living room with a staircase and bookshelves">
  <h1>BEING HOME IN PRAGUE</h1>
  <div class="dots"><span></span><span></span><span></span><span></span></div>
</section>

<form class="booking">
  <h2><i></i>OFFICAL SITE- BEST PRICE GUARANTEED<i></i></h2>
  <div class="field" style="left:113px;top:79px;width:170px">Check in date <svg width="12" height="12" viewBox="0 0 12 12"><rect x="1" y="2" width="10" height="9" fill="none" stroke="#555"/><path d="M1 5h10M4 0v3M8 0v3" stroke="#555"/></svg></div>
  <div class="field" style="left:297px;top:79px;width:170px">Check out date <svg width="12" height="12" viewBox="0 0 12 12"><rect x="1" y="2" width="10" height="9" fill="none" stroke="#555"/><path d="M1 5h10M4 0v3M8 0v3" stroke="#555"/></svg></div>
  <div class="field" style="left:481px;top:79px;width:140px">No of adults <span>&#9662;</span></div>
  <div class="field" style="left:632px;top:79px;width:143px">No of children <span>&#9662;</span></div>
  <div class="field" style="left:789px;top:79px;width:143px">No of infants <span>&#9662;</span></div>
  <div class="field" style="left:113px;top:138px;width:351px">Promotional code</div>
  <div class="or">OR</div>
  <div class="field" style="left:515px;top:138px;width:180px">Select rental unit <span>&#9662;</span></div>
  <div class="btn-check">Check Availbility</div>
</form>

<section class="intro">
  <h2>A DIFFERENT VISION OF<br>TRAVELLING</h2>
  <p>Aliquam molestie, mi et imperdiet euismod, dui purus auctor tellus, et interdum lacus lectus et ante. Sed accumsan sollicitudin sapien, sit amet adipiscing turpis gravida ac. In congue, neque ac lobortis volutpat, libero mauris varius mi, vitae suscipit ipsum ligula vitae risus. Duis aliquam nibh a dui iaculis viverra id a velit.</p>
</section>

<section class="interior">
  <h2>INTERIOR DESIGNED</h2>
  <div class="by">by Maison Lumen</div>
  <p>Aliquam molestie, mi et imperdiet euismod, dui purus auctor tellus, et interdum lacus lectus et ante. Sed accumsan sollicitudin sapien, sit amet adipiscing turpis gravida ac. In congue, neque ac lobortis volutpat, libero mauris varius mi, vitae suscipit ipsum ligula vitae risus. Duis aliquam nibh a dui iaculis viverra id a velit. Vivamus egestas risus in magna varius commodo. Sed semper viverra egestas. Etiam pretium porttitor lectus, vel ornare neque porta volutpat.</p>
  <div class="photo" role="img" aria-label="Photo of a bright white living room with fireplace and staircase"></div>
</section>

<h2 class="featured-title">FEATURED APARTMENTS</h2>

<div class="cards" style="top:1657px">
  <article class="card"><div class="img" role="img" aria-label="Photo of an apartment living room"><span class="meta">1 BEDROOM &nbsp;|&nbsp; MAX 4 PEOPLE</span></div><h3>Brand new luxury living stunning contemporary design</h3><p>Aenean a nibh eget turpis vehicula tempus ac sed massa. Vestibulum dolor nulla, ultrices ac tincidunt sed, laoreet non est.</p><div class="actions"><span class="pill gold">DETAILS</span><span class="pill outline">BOOK NOW</span></div></article>
  <article class="card"><div class="img" role="img" aria-label="Photo of an apartment dining area"><span class="meta">1 BEDROOM &nbsp;|&nbsp; MAX 4 PEOPLE</span></div><h3>Brand new luxury living stunning contemporary design</h3><p>Aenean a nibh eget turpis vehicula tempus ac sed massa. Vestibulum dolor nulla, ultrices ac tincidunt sed, laoreet non est.</p><div class="actions"><span class="pill gold">DETAILS</span><span class="pill outline">BOOK NOW</span></div></article>
  <article class="card"><div class="img" role="img" aria-label="Photo of an apartment bedroom"><span class="meta">1 BEDROOM &nbsp;|&nbsp; MAX 4 PEOPLE</span></div><h3>Brand new luxury living stunning contemporary design</h3><p>Aenean a nibh eget turpis vehicula tempus ac sed massa. Vestibulum dolor nulla, ultrices ac tincidunt sed, laoreet non est.</p><div class="actions"><span class="pill gold">DETAILS</span><span class="pill outline">BOOK NOW</span></div></article>
</div>

<div class="cards" style="top:2089px">
  <article class="card"><div class="img" role="img" aria-label="Photo of an open plan apartment"><span class="meta">1 BEDROOM &nbsp;|&nbsp; MAX 4 PEOPLE</span></div><h3>Brand new luxury living stunning contemporary design</h3><p>Aenean a nibh eget turpis vehicula tempus ac sed massa. Vestibulum dolor nulla, ultrices ac tincidunt sed, laoreet non est.</p><div class="actions"><span class="pill gold">DETAILS</span><span class="pill outline">BOOK NOW</span></div></article>
  <article class="card"><div class="img" role="img" aria-label="Photo of a classic apartment lounge"><span class="meta">1 BEDROOM &nbsp;|&nbsp; MAX 4 PEOPLE</span></div><h3>Brand new luxury living stunning contemporary design</h3><p>Aenean a nibh eget turpis vehicula tempus ac sed massa. Vestibulum dolor nulla, ultrices ac tincidunt sed, laoreet non est.</p><div class="actions"><span class="pill gold">DETAILS</span><span class="pill outline">BOOK NOW</span></div></article>
  <article class="card"><div class="img" role="img" aria-label="Photo of an apartment living room with large windows"><span class="meta">1 BEDROOM &nbsp;|&nbsp; MAX 4 PEOPLE</span></div><h3>Brand new luxury living stunning contemporary design</h3><p>Aenean a nibh eget turpis vehicula tempus ac sed massa. Vestibulum dolor nulla, ultrices ac tincidunt sed, laoreet non est.</p><div class="actions"><span class="pill gold">DETAILS</span><span class="pill outline">BOOK NOW</span></div></article>
</div>

<section class="need">
  <h2>NEED TO KNOW</h2>
  <div class="item" style="left:90px">
    <div class="circle"><svg width="30" height="38" viewBox="0 0 30 38"><rect x="2" y="1" width="26" height="36" fill="#222"/><g fill="#fff"><rect x="7" y="6" width="4" height="4"/><rect x="13" y="6" width="4" height="4"/><rect x="19" y="6" width="4" height="4"/><rect x="7" y="14" width="4" height="4"/><rect x="13" y="14" width="4" height="4"/><rect x="19" y="14" width="4" height="4"/><rect x="7" y="22" width="4" height="4"/><rect x="13" y="22" width="4" height="4"/><rect x="19" y="22" width="4" height="4"/><rect x="12" y="29" width="6" height="8"/></g></svg></div>
    <h3>APARTMENTS</h3>
    <p>Aliquam molestie, mi et imperdiet euismod,<br>dui purus auctor tellus et &nbsp;interdum..</p>
  </div>
  <div class="item" style="left:450px">
    <div class="circle"><svg width="36" height="36" viewBox="0 0 36 36"><circle cx="18" cy="18" r="15" fill="none" stroke="#222" stroke-width="3"/><path d="M18 9v9l6 4" fill="none" stroke="#222" stroke-width="3" stroke-linecap="round"/></svg></div>
    <h3>CHECK -OUT</h3>
    <p>Aliquam molestie, mi et imperdiet euismod,<br>dui purus auctor tellus et &nbsp;interdum..</p>
  </div>
  <div class="item" style="left:801px">
    <div class="circle"><span style="font-size:40px;font-weight:400">$</span></div>
    <h3>RATES</h3>
    <p>Aliquam molestie, mi et imperdiet euismod,<br>dui purus auctor tellus et &nbsp;interdum..</p>
  </div>
</section>

<h2 class="col-title" style="left:76px">NEWS UPDATES</h2>
<article class="news-item" style="top:3085px">
  <div class="date"><div class="m">NOV</div><div class="d">20</div></div>
  <h3>ALIQUAM MOLESTIE MI ET IMPERDIET..</h3>
  <p>Dui purus auctor tellus, et &nbsp;interdum lacus lectus et ante. Sed accumsan sollicitudin sapien, sit amet adipiscing turpis gravida ac...<b>Read More</b></p>
</article>
<article class="news-item" style="top:3215px">
  <div class="date"><div class="m">NOV</div><div class="d">20</div></div>
  <h3>ALIQUAM MOLESTIE MI ET IMPERDIET..</h3>
  <p>Dui purus auctor tellus, et &nbsp;interdum lacus lectus et ante. Sed accumsan sollicitudin sapien, sit amet adipiscing turpis gravida ac...<b>Read More</b></p>
</article>
<div class="divider"></div>

<h2 class="col-title" style="left:630px">HAPPY FAMILIES</h2>
<div class="arrows">
  <svg width="12" height="20" viewBox="0 0 12 20"><path d="M10 2L2 10l8 8" fill="none" stroke="#222" stroke-width="3"/></svg>
  <svg width="12" height="20" viewBox="0 0 12 20"><path d="M2 2l8 8-8 8" fill="none" stroke="#222" stroke-width="3"/></svg>
</div>
<div class="quote-icon">&ldquo;</div>
<p class="testimonial">Vivamus egestas risus in magna varius &nbsp;commodo. Sed semper viverra egestas. Etiam pretium porttitor lectus, vel ornare neque porta volutpat. Vestibulum dolor nulla, ultrices ac tincidunt sed, laoreet non est. Suspendisse lobortis turpis in odio blandit ac interdum lorem euismod...&rdquo;</p>
<div class="avatar" role="img" aria-label="Portrait photo of a guest"></div>
<div class="person"><b>NAME HEADING</b><i>Location</i></div>

<section class="seen">
  <h2>AS SEEN IN</h2>
  <div class="badges">
    <span style="width:110px"></span><span style="width:80px"></span><span style="width:34px;height:34px;border-radius:50%"></span><span style="width:130px;height:18px"></span><span style="width:125px"></span><span style="width:170px"></span>
  </div>
</section>

<div class="newsletter">
  <h2>NEWSLETTER SIGN UP</h2>
  <div class="signup">ENTER EMAIL ADDRESS<span class="go">GO</span></div>
  <div class="follow"><h2>FOLLOW US</h2><span></span><span></span><span></span><span></span><span></span></div>
</div>

<footer class="footer">
  <div class="brand-name">MAISON LUMEN</div>
  <p class="about">Aliquam molestie, mi et imperdiet euismod, dui purus auctor tellus, et interdum lacus lectus et ante. Sed accumsan sollicitudin sapien, sit amet adipiscing turpis gravida ac.</p>
  <div class="sitemap">
    <h4>SITE MAP</h4>
    <ul><li>Apartments</li><li>Location</li><li>Services</li><li>Gallery</li><li>News</li><li>Exclusive Offers &amp; Tours</li><li>For Families</li><li>Contact Us</li></ul>
  </div>
  <div class="contact-info">
    <h4>CONTACT INFO</h4>
    12 Vltavska Street,<br>Prague, 110 00<br>1-800-555-0142<br>info@maisonlumen.com<br>Map Location
  </div>
  <div class="map" role="img" aria-label="Street map showing the apartment location"></div>
</footer>
<div class="copyright">Copyright &copy; 2017. Company Name. All Right reserved</div>

</body>
</html>
```